Venlow Partners
Global Real Estate Investing
Venlow Partners -
Creative Brief
Modern
Ravi Talbert
President
24817 Mobley Lane 2nd Floor Southgate MI 48195
rtalbert@venlowpartners.example
www.venlowpartners.example

```html
<!DOCTYPE html>
<html lang="en">
<head>
<meta charset="utf-8">
<title>Venlow Partners – Stationery Set</title>
<link href="https://fonts.googleapis.com/css2?family=Michroma&family=Open+Sans:wght@400;600;700&display=swap" rel="stylesheet">
<style>
:root{
  --stage:#3b3c3e;
  --paper:#ffffff;
  --paper-shade:#eef1f6;
  --brand:#1d4fae;
  --brand-deep:#123a86;
  --brand-light:#3f74d6;
  --ink:#3a3f4a;
  --faint:#dfe5f0;
  --slate:#5a6272;
}
*{box-sizing:border-box;margin:0;padding:0}
html,body{width:1200px;height:314px;overflow:hidden;background:var(--stage);font-family:"Open Sans",Arial,sans-serif}
.stage{position:relative;width:1200px;height:314px}
.piece{position:absolute;background:var(--paper);box-shadow:0 2px 6px rgba(0,0,0,.45);overflow:hidden}
.wordmark{font-family:"Michroma","Open Sans",sans-serif;color:var(--brand);font-weight:400;letter-spacing:.3px;display:flex;align-items:center;gap:4px;white-space:nowrap}
.wordmark .dot{display:inline-block;border-radius:50%;background:var(--brand);flex:none}

/* master logo */
.logo-master{position:absolute;left:22px;top:28px;width:110px;text-align:center}
.logo-master .dot{width:46px;height:46px;border-radius:50%;background:var(--brand);margin:0 auto 6px}
.logo-master .name{font-family:"Michroma",sans-serif;color:var(--brand-light);font-size:11px;letter-spacing:.5px}
.logo-master .tag{font-size:6px;color:#9fb0cf;margin-top:4px}

/* business cards */
.card{width:110px;height:64px}
.card-front{left:14px;top:152px;background:linear-gradient(135deg,#fff 38%,var(--brand-light) 39%,var(--brand-deep))}
.card-front .person{position:absolute;right:7px;top:7px;text-align:right;color:#fff;font-size:4.5px;line-height:1.5}
.card-front .person b{font-size:5.5px;font-weight:700}
.card-front .rule{position:absolute;left:0;right:0;bottom:10px;height:3px;background:var(--brand)}
.card-logo{left:10px;top:230px;background:linear-gradient(#fff,var(--paper-shade))}
.card-blue{left:134px;top:230px;background:radial-gradient(circle at 40% 40%,var(--brand-light),var(--brand-deep))}
.card .wordmark.centered{position:absolute;left:0;right:0;top:0;bottom:0;justify-content:center;font-size:6px;gap:3px}
.card .wordmark .dot{width:8px;height:8px}
.card-blue .wordmark{color:#fff}
.card-blue .wordmark .dot{background:#fff}

/* letterheads */
.letter{top:22px;width:204px;height:262px}
.letter-one{left:276px}
.letter-two{left:492px}
.letter .wordmark{position:absolute;left:14px;top:16px;font-size:9px}
.letter .wordmark .dot{width:12px;height:12px}
.letter .contact{position:absolute;left:88px;top:14px;font-size:4px;color:var(--slate);line-height:1.5}
.letter .seal{position:absolute;left:72px;top:104px;width:62px;height:62px;border-radius:50%;border:10px solid var(--faint)}
.letter .footer{position:absolute;left:0;right:0;bottom:0;height:10px;background:linear-gradient(90deg,var(--brand-deep),var(--brand-light))}
.letter .footer span{display:block;text-align:center;color:#fff;font-size:3.5px;line-height:10px}

/* compliment slips */
.slip{left:701px;width:188px;height:94px}
.slip-one{top:78px}
.slip-two{top:188px}
.slip .wordmark{position:absolute;left:10px;top:10px;font-size:8px}
.slip .wordmark .dot{width:10px;height:10px}
.slip .seal{position:absolute;left:74px;top:26px;width:40px;height:40px;border-radius:50%;border:7px solid var(--faint)}
.slip .band{position:absolute;left:0;right:0;bottom:0;height:8px;background:var(--brand)}
.slip-two .band{height:5px}

/* envelopes */
.envelope{position:absolute;left:908px;width:282px;height:112px}
.envelope svg{display:block}
.env-back{top:36px}
.env-mid{top:86px}
.env-front{top:160px}
.envelope .wordmark{position:absolute;left:124px;font-size:9px;color:#fff}
.envelope .wordmark .dot{width:12px;height:12px;background:#fff}
.env-back .wordmark{top:14px}
.env-mid .wordmark{top:22px}
</style>
</head>
<body>
<main class="stage">

  <div class="logo-master">
    <div class="dot"></div>
    <div class="name">Venlow Partners</div>
    <div class="tag">Global Real Estate Investing</div>
  </div>

  <section class="piece card card-front">
    <div class="person"><b>Ravi Talbert</b><br>President</div>
    <div class="rule"></div>
  </section>
  <section class="piece card card-logo">
    <div class="wordmark centered"><span class="dot"></span>Venlow Partners</div>
  </section>
  <section class="piece card card-blue">
    <div class="wordmark centered"><span class="dot"></span>Venlow Partners</div>
  </section>

  <section class="piece letter letter-one">
    <div class="wordmark"><span class="dot"></span>Venlow</div>
    <div class="contact">24817 Mobley Lane 2nd Floor<br>Southgate MI 48195<br>rtalbert@venlowpartners.example<br>www.venlowpartners.example</div>
    <div class="seal"></div>
    <div class="footer"><span>www.venlowpartners.example</span></div>
  </section>
  <section class="piece letter letter-two">
    <div class="wordmark"><span class="dot"></span>Venlow</div>
    <div class="seal"></div>
    <div class="footer"><span>www.venlowpartners.example</span></div>
  </section>

  <section class="piece slip slip-one">
    <div class="wordmark"><span class="dot"></span>Venlow</div>
    <div class="seal"></div>
    <div class="band"></div>
  </section>
  <section class="piece slip slip-two">
    <div class="wordmark"><span class="dot"></span>Venlow</div>
    <div class="seal"></div>
    <div class="band"></div>
  </section>

  <section class="envelope env-back">
    <svg width="282" height="112" viewBox="0 0 282 112">
      <rect width="282" height="112" fill="#4a5a7e"/>
      <path d="M0 0 H282 L141 46 Z" fill="#3a4a6c"/>
    </svg>
    <div class="wordmark"><span class="dot"></span>Venlow</div>
  </section>
  <section class="envelope env-mid">
    <svg width="282" height="112" viewBox="0 0 282 112">
      <defs><linearGradient id="envBlue" x1="0" y1="0" x2="1" y2="1"><stop offset="0" stop-color="#3f74d6"/><stop offset="1" stop-color="#123a86"/></linearGradient></defs>
      <rect width="282" height="112" fill="#ffffff"/>
      <path d="M0 0 H282 L141 70 Z" fill="url(#envBlue)"/>
    </svg>
    <div class="wordmark"><span class="dot"></span>Venlow</div>
  </section>
  <section class="envelope env-front">
    <svg width="282" height="112" viewBox="0 0 282 112">
      <rect width="282" height="112" fill="#ffffff"/>
      <path d="M0 0 L141 60 L282 0" fill="none" stroke="#c9d0dd" stroke-width="1.5"/>
      <path d="M0 112 L120 52 M282 112 L162 52" stroke="#dde2ea" stroke-width="1"/>
    </svg>
  </section>

</main>
</body>
</html>
```